Vasko Lumen Entertainment

I need a web design for my Business for better online promotions and services.. The name of my company is Vasko Lumen its a entertainment company music, events, networking and so on.. What I do is help artist create and finish projects such as mix tapes, music videos, and book performances in order to create a platform and i also offer representation to help grow there brands or business... I also work with and help develop independent artists!!!

Target Market(s)

Hip hop and R&B industry

Industry/Entity Type

Entertainment Industry

Number of Pages Required

1 page

Requirements
Must have
• Must display My previous and upcoming work i want people to see the quality I provide in my service.. I have more videos that I want to upload on there to show more work.... I would like to bring all the separate promotions and campaigns that I previously had and currently have all one platform for everybody to see and to find more easily instead having everything so spread out..
Nice to have
• Creativity thats going to compliment my work and quality..

```html
<!DOCTYPE html>
<html lang="en">
<head>
<meta charset="utf-8">
<title>Vasko Lumen Entertainment</title>
<link rel="stylesheet" href="https://fonts.googleapis.com/css2?family=Audiowide&family=Baumans&family=Lato:wght@400;700&family=Oswald:wght@500&display=swap">
<style>
:root{
  --black:#000;
  --red:#ee1f2d;
  --red-dark:#d81a27;
  --red-light:#f2343f;
  --white:#fff;
  --grey:#666;
  --nav-home:#e5177f;
  --nav-albums:#1fa6e0;
  --nav-blog:#c3d82a;
  --nav-events:#6a2b90;
  --nav-artists:#f5b41a;
  --footer:#141414;
}
*{margin:0;padding:0;box-sizing:border-box}
html,body{width:1200px;height:2835px;overflow:hidden;background:var(--black)}
body{position:relative;font-family:"Baumans",sans-serif;color:var(--white)}
.abs{position:absolute}

/* hero */
.hero{left:0;top:0;width:1200px;height:584px;
  background:radial-gradient(ellipse at 48% 35%,#fff8e0 0%,#f0c880 12%,#9a7ab8 30%,#2b5e9a 52%,#0d1e3a 80%,#050810 100%)}
.brand-box{background:#111;border:1px solid #333;display:flex;align-items:center;justify-content:center;gap:10px}
.brand-box .mark{width:14px;height:14px;background:var(--red)}
.brand-name{font-family:"Baumans",sans-serif;color:var(--red);font-size:22px}
.hero .brand-box{left:138px;top:0;width:166px;height:125px}
.main-nav{left:614px;top:0;display:flex}
.main-nav a{width:90px;height:98px;display:flex;flex-direction:column;align-items:center;justify-content:center;gap:8px;
  font-family:"Audiowide",sans-serif;font-size:15px;color:var(--white);text-decoration:none}
.main-nav svg{width:22px;height:22px;fill:var(--white)}
.nav-home{background:var(--nav-home)}
.nav-albums{background:var(--nav-albums)}
.nav-blog{background:var(--nav-blog)}
.nav-events{background:var(--nav-events)}
.nav-artists{background:var(--nav-artists)}
.slide-caption{left:525px;top:457px;width:537px;height:127px;background:rgba(255,255,255,.35);padding:14px 24px}
.slide-caption h2{font-family:"Audiowide",sans-serif;color:var(--red);font-size:23px;font-weight:400;margin-bottom:8px}
.slide-caption p{font-size:15px;line-height:19px}
.slide-dots{right:24px;bottom:8px;display:flex;gap:6px}
.slide-dots span{width:14px;height:14px;border-radius:50%;background:#333}
.slide-dots span.active{background:var(--red)}

/* welcome */
.section-title{font-family:"Audiowide",sans-serif;font-weight:400}
.welcome-title{left:138px;top:648px;font-size:38px;color:var(--red)}
.body-copy{font-size:15.5px;line-height:25px;color:var(--white)}
.welcome-copy{left:138px;top:716px;width:510px}
.service-grid{left:680px;top:637px;width:384px;height:253px;display:grid;grid-template-columns:1fr 1fr;grid-template-rows:1fr 1fr}
.service-grid div{display:flex;align-items:center;justify-content:center}
.service-grid div:nth-child(1),.service-grid div:nth-child(4){background:var(--red)}
.service-grid div:nth-child(2),.service-grid div:nth-child(3){background:var(--red-light)}
.service-grid svg{width:60px;height:60px;fill:none;stroke:var(--white);stroke-width:5}

/* work */
.work-title{left:0;width:1200px;top:972px;text-align:center;font-size:38px}
.album{width:297px;height:234px}
.album-art{height:202px}
.album-bar{height:32px;background:var(--red);display:flex;align-items:center;justify-content:space-between;padding:0 12px;
  font-family:"Audiowide",sans-serif;font-size:16px}
.album-bar svg{width:22px;height:22px}
.art-1{background:linear-gradient(135deg,#1b3c8c,#3a7fd0 45%,#6a4fa0)}
.art-2{background:linear-gradient(135deg,#b01040,#e8407a 50%,#5a1020)}
.art-3{background:linear-gradient(135deg,#2a1410,#6a3020 50%,#1a0c0a)}
.art-4{background:linear-gradient(180deg,#d8d8d8,#8a8a8a 50%,#4a4a4a)}
.art-5{background:linear-gradient(180deg,#1a1c28,#3c3e52 50%,#5a1a1e)}
.more-songs{right:136px;top:1605px;display:flex;align-items:center;gap:10px;color:var(--red);font-family:"Oswald",sans-serif;font-size:19px;letter-spacing:1px}
.more-songs svg{width:30px;height:30px}

/* team */
.team-title{left:138px;top:1690px;font-size:38px}
.team-card{width:457px;height:191px;background:var(--white);padding:22px 26px 0 104px}
.avatar{left:25px;top:22px;width:66px;height:66px;border-radius:50%}
.av-1{background:linear-gradient(#6a5a40,#2a2018)}
.av-2{background:linear-gradient(#d8c8a8,#9a8060)}
.av-3{background:linear-gradient(#7ab040,#3a5a20)}
.av-4{background:linear-gradient(#8a5a40,#3a2010)}
.team-card h3{font-family:"Audiowide",sans-serif;font-weight:400;font-size:16px;color:var(--red);margin-bottom:8px}
.team-card p{font-family:"Lato",sans-serif;font-size:11.5px;line-height:22px;color:var(--grey)}
.team-card svg{margin-top:6px;width:18px;height:18px}

/* event */
.event-title{left:172px;top:2300px;font-size:34px}
.event-copy{left:172px;top:2364px;width:510px}
.event-photo{left:726px;top:2264px;width:327px;height:259px;background:linear-gradient(180deg,#c8c8c8,#7a6a5a 55%,#3a3a3a)}
.event-bar{left:726px;top:2523px;width:327px;height:30px;background:var(--red);display:flex;align-items:center;justify-content:space-between;padding:0 14px;font-family:"Audiowide",sans-serif;font-size:16px}
.event-bar svg{width:34px;height:16px}

/* footer */
.footer{left:0;top:2604px;width:1200px;height:184px;background:linear-gradient(180deg,#1c1c1c,#0a0a0a)}
.footer-edge{left:0;top:0;width:1200px;height:16px}
.footer .brand-box{left:172px;top:42px;width:164px;height:126px}
.footer h4{font-family:"Oswald",sans-serif;font-weight:500;font-size:32px;letter-spacing:1px}
.footer-nav-title{left:395px;top:50px}
.footer-links{left:395px;top:104px;display:grid;grid-template-columns:85px 80px;font-family:"Lato",sans-serif;font-weight:700;font-size:13px;letter-spacing:2px;line-height:20px}
.connect-title{left:662px;top:50px}
.subscribe{left:665px;top:120px;display:flex;height:47px}
.subscribe .email{width:278px;background:var(--red);padding:0 20px;display:flex;align-items:center;font-family:"Lato",sans-serif;font-weight:700;font-size:14px;letter-spacing:1px}
.subscribe .btn{width:136px;background:var(--white);color:#222;display:flex;align-items:center;justify-content:center;font-family:"Lato",sans-serif;font-size:20px}
.copyright{left:0;top:2788px;width:1200px;height:47px;background:var(--red);display:flex;align-items:center;justify-content:center;font-family:"Lato",sans-serif;font-weight:700;font-size:15px;letter-spacing:1px}
</style>
</head>
<body>

<header class="hero abs" role="img" aria-label="Concert stage with spotlights and a cheering crowd">
</header>
<div class="brand-box abs" style="left:138px;top:0;width:166px;height:125px"><span class="mark"></span><span class="brand-name">Vasko Lumen</span></div>

<nav class="main-nav abs">
  <a class="nav-home" href="#"><svg viewBox="0 0 24 24"><path d="M12 2 1 12h3v10h6v-6h4v6h6V12h3z"/></svg>Home</a>
  <a class="nav-albums" href="#"><svg viewBox="0 0 24 24"><path d="M2 4h20v16H2zM4 6v10l5-5 4 4 3-3 4 4V6zm12 1a2 2 0 1 1 0 4 2 2 0 0 1 0-4z" fill-rule="evenodd"/></svg>Albums</a>
  <a class="nav-blog" href="#"><svg viewBox="0 0 24 24"><path d="M2 2h10l10 10-10 10L2 12zm5 3a2 2 0 1 0 0 4 2 2 0 0 0 0-4z" fill-rule="evenodd"/></svg>Blog</a>
  <a class="nav-events" href="#"><svg viewBox="0 0 24 24"><path d="M3 5h18v16H3zm2 5v9h14v-9zM7 2h2v4H7zm8 0h2v4h-2z" fill-rule="evenodd"/></svg>Events</a>
  <a class="nav-artists" href="#"><svg viewBox="0 0 24 24"><circle cx="12" cy="7" r="5"/><path d="M3 22c0-6 4-9 9-9s9 3 9 9z"/></svg>Artists</a>
</nav>

<div class="slide-caption abs">
  <h2>Consectetur adipisicing elit</h2>
  <p>Lorem ipsum dolor sit amet, consectetur adipisicing elit,<br>sed do eiusmod tempor incididunt ut labore et dolore magna<br>aliqua. Ut enim ad minim veniam, quis nostru.</p>
  <div class="slide-dots abs"><span></span><span></span><span class="active"></span></div>
</div>

<h1 class="section-title welcome-title abs">Welcome</h1>
<p class="body-copy welcome-copy abs">Lorem ipsum dolor sit amet, consectetur adipisicing elit,<br>sed do eiusmod tempor incididunt ut labore et dolore magna<br>aliqua. Ut enim ad minim veniam, quis nostru.<br>Lorem ipsum dolor sit amet, consectetur adipisicing elit,<br>sed do eiusmod tempor incididunt ut labore et dolore magna<br>aliqua. Ut enim ad minim veniam, quis nostru.</p>

<div class="service-grid abs">
  <div><svg viewBox="0 0 60 60"><circle cx="20" cy="40" r="12"/><path d="M28 32 52 8M46 6l8 8"/><circle cx="20" cy="40" r="3"/></svg></div>
  <div><svg viewBox="0 0 60 60"><path d="M8 42h44v10H8zM18 42V32h24v10"/><circle cx="34" cy="14" r="6"/><path d="M34 20v12"/></svg></div>
  <div><svg viewBox="0 0 60 60"><path d="M10 50V30M20 50V16M30 50V24M40 50V10M50 50V34"/></svg></div>
  <div><svg viewBox="0 0 60 60"><path d="M10 40V30a20 20 0 0 1 40 0v10"/><path d="M8 34h10v18H8zM42 34h10v18H42z" fill="#fff"/></svg></div>
</div>

<h2 class="section-title work-title abs">Our Work</h2>

<div class="album abs" style="left:138px;top:1055px"><div class="album-art art-1" role="img" aria-label="Album cover, club lights"></div><div class="album-bar">My Album<svg viewBox="0 0 22 22"><circle cx="11" cy="11" r="9" fill="none" stroke="#fff" stroke-width="2"/><path d="M9 7l5 4-5 4z" fill="#fff"/></svg></div></div>
<div class="album abs" style="left:465px;top:1055px;width:289px"><div class="album-art art-2" role="img" aria-label="Album cover, artist portrait in pink light"></div><div class="album-bar">My Album<svg viewBox="0 0 22 22"><circle cx="11" cy="11" r="9" fill="none" stroke="#fff" stroke-width="2"/><path d="M9 7l5 4-5 4z" fill="#fff"/></svg></div></div>
<div class="album abs" style="left:784px;top:1055px;width:280px"><div class="album-art art-3" role="img" aria-label="Album cover, performer on stage"></div><div class="album-bar">My Album<svg viewBox="0 0 22 22"><circle cx="11" cy="11" r="9" fill="none" stroke="#fff" stroke-width="2"/><path d="M9 7l5 4-5 4z" fill="#fff"/></svg></div></div>
<div class="album abs" style="left:138px;top:1328px"><div class="album-art art-4" role="img" aria-label="Music video still, group of artists"></div><div class="album-bar">My Album<svg viewBox="0 0 22 22"><circle cx="11" cy="11" r="9" fill="none" stroke="#fff" stroke-width="2"/><path d="M9 7l5 4-5 4z" fill="#fff"/></svg></div></div>
<div class="album abs" style="left:465px;top:1328px;width:289px"><div class="album-art art-5" role="img" aria-label="Music video still, artist and car at night"></div><div class="album-bar">My Album<svg viewBox="0 0 22 22"><circle cx="11" cy="11" r="9" fill="none" stroke="#fff" stroke-width="2"/><path d="M9 7l5 4-5 4z" fill="#fff"/></svg></div></div>
<div class="album abs" style="left:784px;top:1328px;width:280px"><div class="album-art art-4" role="img" aria-label="Music video still, group of artists"></div><div class="album-bar">My Album<svg viewBox="0 0 22 22"><circle cx="11" cy="11" r="9" fill="none" stroke="#fff" stroke-width="2"/><path d="M9 7l5 4-5 4z" fill="#fff"/></svg></div></div>

<a class="more-songs abs">CLICK HERE FOR MORE SONGS<svg viewBox="0 0 30 30"><circle cx="15" cy="15" r="13" fill="none" stroke="#ee1f2d" stroke-width="2.5"/><path d="M15 8v14M8 15h14" stroke="#ee1f2d" stroke-width="2.5"/></svg></a>

<h2 class="section-title team-title abs">Team</h2>

<article class="team-card abs" style="left:138px;top:1761px">
  <div class="avatar av-1 abs" role="img" aria-label="Team member portrait"></div>
  <h3>It is a long established fact that</h3>
  <p>Kosertos lertyasea deeraeser miasera ritise<br>dolsert ferdos coplicabo nerafoes osety u lasec voserat.<br>nikertyode osetkertyptoiades goertoyse.nikertyade<br>osetkertyptoiades goertayse</p>
  <svg viewBox="0 0 18 18"><circle cx="9" cy="9" r="8"/><path d="M5 9h7M9 6l3 3-3 3" stroke="#fff" stroke-width="1.8" fill="none"/></svg>
</article>
<article class="team-card abs" style="left:622px;top:1761px">
  <div class="avatar av-2 abs" role="img" aria-label="Team member portrait"></div>
  <h3>It is a long established fact that</h3>
  <p>Kosertos lertyasea deeraeser miasera ritise<br>dolsert ferdos coplicabo nerafoes osety u lasec voserat.<br>nikertyode osetkertyptoiades goertoyse.nikertyade<br>osetkertyptoiades goertayse</p>
  <svg viewBox="0 0 18 18"><circle cx="9" cy="9" r="8"/><path d="M5 9h7M9 6l3 3-3 3" stroke="#fff" stroke-width="1.8" fill="none"/></svg>
</article>
<article class="team-card abs" style="left:138px;top:1988px">
  <div class="avatar av-3 abs" role="img" aria-label="Team member portrait"></div>
  <h3>It is a long established fact that</h3>
  <p>Kosertos lertyasea deeraeser miasera ritise<br>dolsert ferdos coplicabo nerafoes osety u lasec voserat.<br>nikertyode osetkertyptoiades goertoyse.nikertyade<br>osetkertyptoiades goertayse</p>
  <svg viewBox="0 0 18 18"><circle cx="9" cy="9" r="8"/><path d="M5 9h7M9 6l3 3-3 3" stroke="#fff" stroke-width="1.8" fill="none"/></svg>
</article>
<article class="team-card abs" style="left:622px;top:1988px">
  <div class="avatar av-4 abs" role="img" aria-label="Team member portrait"></div>
  <h3>It is a long established fact that</h3>
  <p>Kosertos lertyasea deeraeser miasera ritise<br>dolsert ferdos coplicabo nerafoes osety u lasec voserat.<br>nikertyode osetkertyptoiades goertoyse.nikertyade<br>osetkertyptoiades goertayse</p>
  <svg viewBox="0 0 18 18"><circle cx="9" cy="9" r="8"/><path d="M5 9h7M9 6l3 3-3 3" stroke="#fff" stroke-width="1.8" fill="none"/></svg>
</article>

<h2 class="section-title event-title abs">Upcoming Event</h2>
<p class="body-copy event-copy abs">Lorem ipsum dolor sit amet, consectetur adipisicing elit,<br>sed do eiusmod tempor incididunt ut labore et dolore magna<br>aliqua. Ut enim ad minim veniam, quis nostru.<br>Lorem ipsum dolor sit amet, consectetur adipisicing elit,<br>sed do eiusmod tempor incididunt ut labore et dolore magna<br>aliqua. Ut enim ad minim veniam, quis nostru.</p>
<div class="event-photo abs" role="img" aria-label="Photo of three artists for the upcoming event"></div>
<div class="event-bar abs">Events<svg viewBox="0 0 34 16"><path d="M10 2 4 8l6 6M24 2l6 6-6 6" stroke="#fff" stroke-width="3" fill="none"/></svg></div>

<footer class="footer abs">
  <svg class="footer-edge abs" viewBox="0 0 1200 16" preserveAspectRatio="none"><path d="M0 0h1200v16z" fill="none"/><path d="M0 0 L1200 0 L1200 4 L0 4z" fill="#000"/><path d="M0 4 L8 14 L16 4 L24 14 L32 4 L40 14 L48 4 L56 14 L64 4 L72 14 L80 4 L88 14 L96 4 L104 14 L112 4 L120 14 L128 4 L136 14 L144 4 L152 14 L160 4 L168 14 L176 4 L184 14 L192 4 L200 14 L208 4 L216 14 L224 4 L232 14 L240 4 L248 14 L256 4 L264 14 L272 4 L280 14 L288 4 L296 14 L304 4 L312 14 L320 4 L328 14 L336 4 L344 14 L352 4 L360 14 L368 4 L376 14 L384 4 L392 14 L400 4 L408 14 L416 4 L424 14 L432 4 L440 14 L448 4 L456 14 L464 4 L472 14 L480 4 L488 14 L496 4 L504 14 L512 4 L520 14 L528 4 L536 14 L544 4 L552 14 L560 4 L568 14 L576 4 L584 14 L592 4 L600 14 L608 4 L616 14 L624 4 L632 14 L640 4 L648 14 L656 4 L664 14 L672 4 L680 14 L688 4 L696 14 L704 4 L712 14 L720 4 L728 14 L736 4 L744 14 L752 4 L760 14 L768 4 L776 14 L784 4 L792 14 L800 4 L808 14 L816 4 L824 14 L832 4 L840 14 L848 4 L856 14 L864 4 L872 14 L880 4 L888 14 L896 4 L904 14 L912 4 L920 14 L928 4 L936 14 L944 4 L952 14 L960 4 L968 14 L976 4 L984 14 L992 4 L1000 14 L1008 4 L1016 14 L1024 4 L1032 14 L1040 4 L1048 14 L1056 4 L1064 14 L1072 4 L1080 14 L1088 4 L1096 14 L1104 4 L1112 14 L1120 4 L1128 14 L1136 4 L1144 14 L1152 4 L1160 14 L1168 4 L1176 14 L1184 4 L1192 14 L1200 4z" fill="#fff"/></svg>
  <div class="brand-box abs"><span class="mark"></span><span class="brand-name">Vasko Lumen</span></div>
  <h4 class="footer-nav-title abs">NAVIGATION</h4>
  <div class="footer-links abs"><span>HOME</span><span>NEWS</span><span>MUSIC</span><span></span><span>ARTISTE</span></div>
  <h4 class="connect-title abs">CONNECT WITH MUSIC</h4>
  <form class="subscribe abs"><span class="email">Type your email</span><span class="btn">Subscribe</span></form>
</footer>

<div class="copyright abs">Copyright 2017 Vasko Lumen.</div>

</body>
</html>
```